Quorvex clinic business card - double sided for young clinic

I require business cards for my aesthetic clinic specialising in the below treatments. I would like the cards to be modern as my clinic base are young 22-35 years old. I require my logo on it and would like the edges to be rounded.

I have an aesthetic clinic specialising in :
Quorvex
Lip Enhancement
Chemical Peels
Facial Fillers
Non Surgical Face Lift

I would the cards to have the following information on them:
My logo - (in grey/silver)
address
Phone number
services

Colours :
White/grey/silver and red

a nice image on there, perhaps a set of lips as this is a main service i deliver

Company Name: PDA Address: 52 Farrowmere Road, 4 Brackwell High Street, KT9 4WQ Phone: 0208 794 2160 Website: www.penningtondoweaesthetics.co.uk

Target Market(s)

clinics 22-45 years old mainly female

Industry/Entity Type

Business

Contact Information for Business Card

as above

Requirements
Must have
• logo
• Address
• Email
• Phone number
• Services i offer
Nice to have
• images

```html
<!DOCTYPE html>
<html lang="en">
<head>
<meta charset="utf-8">
<title>PDA Aesthetics – Business Card</title>
<link rel="stylesheet" href="https://fonts.googleapis.com/css2?family=Old+Standard+TT:wght@400;700&display=swap">
<style>
  :root {
    --page: #ecebea;
    --card-grey-light: #8a8a8c;
    --card-grey-dark: #4b4b4d;
    --band-grey: #5d5d60;
    --lace-grey: #a9a9ab;
    --text-light: #f4f4f4;
    --lip-light: #f3c9b8;
    --lip-mid: #e79a92;
    --lip-deep: #c9645f;
    --skin: #f0c8b0;
    --shadow: rgba(0,0,0,0.22);
  }
  * { margin: 0; padding: 0; box-sizing: border-box; }
  html, body {
    width: 1200px; height: 1023px; overflow: hidden;
    background: var(--page);
    font-family: "Old Standard TT", Georgia, serif;
  }
  .sheet {
    width: 1200px; height: 1023px;
    display: flex; flex-direction: column; align-items: center; justify-content: center;
    gap: 60px;
  }
  .card {
    position: relative;
    width: 700px; height: 400px;
    border-radius: 28px;
    overflow: hidden;
    box-shadow: 0 10px 28px var(--shadow);
  }

  /* Back side */
  .card-back {
    background: linear-gradient(135deg, var(--card-grey-light), var(--card-grey-dark));
    color: var(--text-light);
  }
  .lace-band {
    position: absolute; left: 0; right: 0; height: 46px;
    background: linear-gradient(180deg, var(--lace-grey), #959597);
    opacity: 0.55;
  }
  .lace-band.top { top: 28px; }
  .lace-band.bottom { bottom: 28px; }
  .contact {
    position: absolute; inset: 0;
    display: flex; flex-direction: column; align-items: center; justify-content: center;
    text-align: center; gap: 8px;
    font-size: 19px; letter-spacing: 0.5px;
  }
  .contact .phone { font-weight: 700; font-size: 21px; margin-bottom: 14px; }
  .contact .address { margin-top: 22px; font-size: 20px; }

  /* Front side */
  .card-front { background: var(--skin); }
  .lip-photo {
    position: absolute; left: 0; top: 0; right: 0; bottom: 96px;
    background:
      radial-gradient(ellipse 60% 42% at 50% 52%, var(--lip-mid), var(--lip-deep) 55%, transparent 75%),
      linear-gradient(180deg, var(--lip-light), var(--skin));
  }
  .services-band {
    position: absolute; left: 0; right: 0; bottom: 0; height: 96px;
    background: var(--band-grey);
    color: var(--text-light);
    display: flex; flex-direction: column; justify-content: center; align-items: center;
    gap: 6px;
    font-size: 20px; letter-spacing: 1px;
  }
  .brand {
    position: absolute; left: 0; right: 0; top: 70px;
    display: flex; align-items: center; justify-content: center; gap: 26px;
    color: var(--text-light);
    font-weight: 400;
  }
  .brand-mark {
    width: 118px; height: 118px; border-radius: 50%;
    border: 3px solid var(--text-light);
    display: flex; align-items: center; justify-content: center;
    font-size: 38px; letter-spacing: 3px;
  }
  .brand-name { display: flex; flex-direction: column; line-height: 1; }
  .brand-name .first { font-size: 24px; letter-spacing: 6px; }
  .brand-name .second { font-size: 50px; letter-spacing: 5px; margin-top: 6px; }
</style>
</head>
<body>
<main class="sheet">
  <section class="card card-back" aria-label="Business card back">
    <div class="lace-band top" role="img" aria-label="Decorative lace border"></div>
    <div class="lace-band bottom" role="img" aria-label="Decorative lace border"></div>
    <div class="contact">
      <p class="phone">0208 794 2160</p>
      <p class="email">info@penningtondoweaesthetics.co.uk</p>
      <p class="web">www.penningtondoweaesthetics.co.uk</p>
      <p class="address">52 Farrowmere Road, 4 Brackwell High Street, KT9 4WQ</p>
    </div>
  </section>

  <section class="card card-front" aria-label="Business card front">
    <div class="lip-photo" role="img" aria-label="Close-up photograph of glossy pink lips"></div>
    <div class="brand">
      <div class="brand-mark">PDA</div>
      <div class="brand-name">
        <span class="first">PENNINGTON DOWE</span>
        <span class="second">AESTHETICS</span>
      </div>
    </div>
    <div class="services-band">
      <p>Quorvex | Lip Enhancement | Chemical Peels</p>
      <p>Facial Fillers | Non Surgical Face Lift</p>
    </div>
  </section>
</main>
</body>
</html>
```